Family Photography A5 Invitation to prospective clients

A restaurant will give me public space at their entrance to promote my family photography. I need an A5 vertical layout design for a card to 'invite' potential clients to call me. I am a portrait photographer in Perth, Western Australia. The A5 cards will be taken away by potential clients. They are encouraged to call the studio to register their interest with a view to having a very beautiful family portrait in the studio or on location. This will save the family $250 because the fee will be waived. Locations for photography can include a sunset at the famous Tarrington Beach or parks in the Western Suburbs of Perth. Prefer Indesign work file so that I can change images for reprints later. Will be happy to give extra ongoing work to the successful designer on future projects. I'm happy to take positional images in the design and change them later.

Target Market(s)

Women mainly in the 30 to 45 years age group

Industry/Entity Type

Restaurant

Font styles to use
Sans Serif

Requirements
Must have
• Call to action and lively design that gets attention. Prefer to have some similarity with style of web site wrenlightstudio.com.au
Nice to have
• Prefer not to have the look of fake 'competitions' but rather an invitation to have a beautiful experience and with the opportunity to purchase a beautiful piece of art that celebrates their family. See word doc for previous idea with 'win a portrait...' Some of the words might be useful. More here... Dean Marlow’s photography hangs on thousands of walls in Perth’s homes. His family portraits are not so much photographs as works of art, each one perfect in its own way, a unique interplay of light, shade, colour and composition. They’re the ones that make people say more than just, ‘Oh, nice’. They make people linger and say, ‘Wow, amazing!’.
Should not have
• Avoid too much emphasis on cost. I am not competing on cost, but rather trying to inspire the potential client. See word doc for previous idea with 'win a portrait...' Some of the words might be useful.

```html
<!DOCTYPE html>
<html lang="en">
<head>
<meta charset="utf-8">
<title>About Dean Marlow – Wrenlight Studio</title>
<link href="https://fonts.googleapis.com/css2?family=Open+Sans:wght@400;600;700&family=Oswald:wght@500&display=swap" rel="stylesheet">
<style>
  :root{
    --backdrop:#959595;
    --paper:#ffffff;
    --paper-fade:#dedede;
    --ink:#474747;
    --ink-soft:#5c5c5c;
    --accent:#6b9a3f;
    --decor:#ececec;
    --quote:#d4d4d4;
    --photo-dark:#1b1b1b;
    --photo-mid:#4a4a4a;
  }
  *{box-sizing:border-box;margin:0;padding:0}
  html,body{width:1200px;height:900px;overflow:hidden;background:var(--backdrop)}
  body{position:relative;font-family:"Open Sans",Arial,sans-serif;color:var(--ink)}
  .card{position:absolute;left:284px;top:6px;width:632px;height:887px;
    background:linear-gradient(to bottom,var(--paper) 0,var(--paper) 76%,var(--paper-fade) 100%);overflow:hidden}
  .decor-area{position:absolute;left:356px;top:20px;width:300px;height:310px;border-radius:50%;
    background:radial-gradient(ellipse at 55% 50%,var(--decor) 0,rgba(236,236,236,.6) 55%,rgba(255,255,255,0) 72%)}
  .decor-quote{position:absolute;left:462px;top:236px;font-size:140px;line-height:1;color:var(--quote);font-weight:700}
  .brand{position:absolute;left:50px;top:78px;display:flex;align-items:center;gap:7px}
  .brand-dot{width:16px;height:16px;border-radius:50%;background:var(--ink-soft)}
  .brand-name{font-size:13px;font-weight:600;color:var(--ink-soft);line-height:1.15;width:70px}
  .heading{position:absolute;right:50px;top:80px;text-align:right;color:var(--ink)}
  .heading-kicker{font-size:13px;font-weight:600;letter-spacing:4px}
  .heading-name{font-size:20px;font-weight:600;letter-spacing:5.5px;margin-top:2px}
  .copy{position:absolute;left:50px;width:532px;font-size:13.4px;line-height:17px;letter-spacing:.2px;
    text-align:justify;hyphens:auto;-webkit-hyphens:auto;color:var(--ink)}
  .copy p{text-indent:52px}
  .copy-intro{top:153px}
  .copy-offer{top:368px}
  .copy-cta{top:443px}
  .distinction{position:absolute;left:96px;top:268px;display:flex;align-items:center}
  .badge{width:130px;height:66px;background:#d6d6d6;border-radius:4px}
  .divider{width:1px;height:70px;background:#bfbfbf;margin:0 9px 0 13px}
  .distinction-text{font-size:12px;line-height:18px;color:var(--accent);width:220px}
  .photo{position:absolute;background:radial-gradient(ellipse at 55% 45%,var(--photo-mid),var(--photo-dark) 70%)}
  .p1{left:133px;top:538px;width:180px;height:85px}
  .p2{left:316px;top:538px;width:183px;height:85px}
  .p3{left:56px;top:626px;width:166px;height:104px}
  .p4{left:225px;top:626px;width:164px;height:104px}
  .p5{left:393px;top:626px;width:183px;height:104px}
  .call-tab{position:absolute;left:396px;top:690px;width:22px;height:12px;background:var(--accent);border-radius:2px}
  .call-box{position:absolute;left:200px;top:697px;width:233px;height:115px;background:var(--paper);
    border:1px solid #cfcfcf;border-radius:12px;box-shadow:0 1px 4px rgba(0,0,0,.2)}
  .call-photo{position:absolute;left:4px;top:12px;width:100px;height:100px;border-radius:50%;
    border:4px solid #e2e2e2;background:linear-gradient(to bottom,#b9c3cc,#6d6d66)}
  .call-label{position:absolute;left:104px;top:8px;width:116px;text-align:right;font-size:23px;color:var(--ink-soft);line-height:28px}
  .call-now{position:absolute;left:104px;top:36px;width:116px;text-align:right;font-size:30px;color:var(--ink-soft);line-height:34px}
  .call-rule{position:absolute;left:110px;top:74px;width:110px;height:1px;background:#cfcfcf}
  .call-phone{position:absolute;left:106px;top:78px;width:116px;text-align:center;font-family:"Oswald",Arial,sans-serif;font-weight:500;font-size:20px;letter-spacing:.5px;color:var(--accent)}
  .site{position:absolute;left:0;width:632px;top:828px;text-align:center;font-size:14px;font-weight:600;letter-spacing:.8px;color:var(--ink-soft)}
</style>
</head>
<body>
<main class="card">
  <div class="decor-area" role="img" aria-label="Faint decorative background shape"></div>
  <div class="decor-quote" aria-hidden="true">”</div>

  <div class="brand"><span class="brand-dot"></span><span class="brand-name">Wrenlight Studio</span></div>

  <header class="heading">
    <div class="heading-kicker">ABOUT</div>
    <h1 class="heading-name">DEAN MARLOW</h1>
  </header>

  <section class="copy copy-intro" lang="en">
    <p>Dean Marlow’s photography hangs on thousands of walls in Perth’s homes. His family portraits are not so much photographs as works of art, each one perfect in its own way, a unique interplay of light, shade, colour and composition. They’re the ones that make people say more than just, ‘Oh, nice’. They make people linger and say, ‘Wow, amazing!’.</p>
  </section>

  <div class="distinction">
    <div class="badge" role="img" aria-label="Professional guild badge"></div>
    <div class="divider"></div>
    <p class="distinction-text">In 1996, He was Recognised by the Australasian Guild of Portrait Artists (AGPA) with the Distinction of Master Photographer.</p>
  </div>

  <section class="copy copy-offer" lang="en">
    <p>&amp; This is your opportunity to possess the most beautiful photographic art of yourself and your loved ones. We’re looking forward to giving you the experience of a photography session you’ll never forget.</p>
  </section>

  <section class="copy copy-cta" lang="en">
    <p>Call Dean today to register your interest with a view to having a very beautiful family portrait in the studio or on locations which include a sunset at the famous Tarrington Beach or parks in the Western Suburbs of Perth..</p>
  </section>

  <div class="photo p1" role="img" aria-label="Black and white portrait of a girl playing violin"></div>
  <div class="photo p2" role="img" aria-label="Black and white portrait of a father and adult son"></div>
  <div class="photo p3" role="img" aria-label="Black and white portrait of a father with two children"></div>
  <div class="photo p4" role="img" aria-label="Black and white portrait of a mother and young daughter"></div>
  <div class="photo p5" role="img" aria-label="Black and white portrait of three young men"></div>

  <div class="call-tab"></div>
  <div class="call-box">
    <div class="call-photo" role="img" aria-label="Photographer riding a bicycle"></div>
    <div class="call-label">Call Dean</div>
    <div class="call-now">NOW</div>
    <div class="call-rule"></div>
    <div class="call-phone">0400 555 218</div>
  </div>

  <div class="site">WWW.WRENLIGHTSTUDIO.COM.AU</div>
</main>
</body>
</html>
```